Harborline Works Buisness Cards

Provide a business card layout

Peter Landry
PO Box 915
Alderbrook MA 01999
peter@hworksllc-example.com

Industry/Entity Type

Business

Font styles to use
Serif

Colors
f04a50

```html
<!DOCTYPE html>
<html lang="en">
<head>
<meta charset="utf-8">
<title>Harborline Works – Business Card</title>
<link href="https://fonts.googleapis.com/css2?family=Libre+Baskerville:wght@400;700&family=Tinos:wght@400;700&display=swap" rel="stylesheet">
<style>
  :root {
    --backdrop: #3a1416;
    --card: #ffffff;
    --ink: #111111;
    --accent-red: #9e1b1f;
    --accent-gold: #e9a53a;
    --band: #0d0d0d;
    --band-text: #f2f2f2;
    --faint: #f6ece4;
  }
  * { margin: 0; padding: 0; box-sizing: border-box; }
  html, body {
    width: 1200px; height: 800px; overflow: hidden;
    background: var(--backdrop);
  }
  .card {
    position: absolute; left: 150px; top: 130px;
    width: 900px; height: 540px;
    background: var(--card);
    overflow: hidden;
    box-shadow: 0 20px 50px rgba(0,0,0,.5);
  }
  .card__watermark {
    position: absolute; right: -80px; top: 40px;
    width: 420px; height: 420px; border-radius: 50%;
    background: var(--faint);
  }
  .brand {
    position: absolute; left: 70px; top: 120px;
    display: flex; align-items: center; gap: 18px;
  }
  .brand__dot {
    width: 44px; height: 44px; border-radius: 50%;
    background: var(--accent-red);
  }
  .brand__name {
    font-family: "Tinos", "Times New Roman", serif;
    font-weight: 700; font-size: 40px; letter-spacing: 1px;
    color: var(--ink);
  }
  .person {
    position: absolute; left: 70px; top: 255px;
    font-family: "Libre Baskerville", Georgia, serif;
    font-weight: 700; font-size: 34px;
    color: var(--accent-gold);
  }
  .contacts {
    position: absolute; left: 70px; top: 320px;
    list-style: none;
    font-family: "Tinos", "Times New Roman", serif;
    font-size: 30px; color: var(--ink);
  }
  .contacts__item { display: flex; align-items: center; gap: 14px; height: 42px; white-space: nowrap; }
  .contacts__icon { width: 26px; height: 26px; flex: none; }
  .card__rule {
    position: absolute; left: 0; right: 0; bottom: 62px;
    height: 6px; background: var(--accent-red);
  }
  .card__band {
    position: absolute; left: 0; right: 0; bottom: 0; height: 62px;
    background: var(--band);
    display: flex; align-items: center; justify-content: flex-end;
    padding-right: 60px;
    font-family: "Tinos", "Times New Roman", serif;
    font-size: 20px; color: var(--band-text);
  }
</style>
</head>
<body>
  <article class="card">
    <div class="card__watermark" aria-hidden="true"></div>

    <header class="brand">
      <span class="brand__dot" aria-hidden="true"></span>
      <span class="brand__name">Harborline Works</span>
    </header>

    <h1 class="person">Peter Landry</h1>

    <ul class="contacts">
      <li class="contacts__item">
        <svg class="contacts__icon" viewBox="0 0 24 24" aria-hidden="true">
          <rect x="6" y="2" width="12" height="20" rx="2" fill="none" stroke="#9e1b1f" stroke-width="2"/>
          <rect x="8.5" y="5" width="7" height="7" fill="#9e1b1f"/>
          <circle cx="12" cy="17.5" r="1.5" fill="#9e1b1f"/>
        </svg>
        <span>555 010 4482</span>
      </li>
      <li class="contacts__item">
        <svg class="contacts__icon" viewBox="0 0 24 24" aria-hidden="true">
          <rect x="2" y="5" width="20" height="14" rx="1.5" fill="#9e1b1f"/>
          <path d="M3 6.5 L12 13 L21 6.5" fill="none" stroke="#fff" stroke-width="1.8"/>
        </svg>
        <span>peter@hworksllc-example.com</span>
      </li>
      <li class="contacts__item">
        <svg class="contacts__icon" viewBox="0 0 24 24" aria-hidden="true">
          <path d="M12 3 L2 12 H5 V21 H10 V15 H14 V21 H19 V12 H22 Z" fill="#9e1b1f"/>
        </svg>
        <span>PO Box 915, Alderbrook MA 01999</span>
      </li>
    </ul>

    <div class="card__rule" aria-hidden="true"></div>
    <footer class="card__band">MA Builders License CS 041172</footer>
  </article>
</body>
</html>
```